A professional business to business web site for a contract agency called VONTAREX.

We need a very clean, very professional web site created for business to business. It is an informational web site with 3 pages. We are a company that offers contract employee placements into primarily the pharmaceutical industry. I have attached a file that describes the company more fully.

Hi,

I'm sorry if I wasn't clear, but I need to have the HTML pages created so I can just upload the files you give me to the web hosting site.

Please let me know if you have any questions.

Thanks for working on my project!

Hello,

I didn't put this in the description, but I would need the web site set up on the web hosting site as well.  The web hosting site is abrightkettle.  I want a copy of all the files as well.

Thanks,
Miles

Reason: I'm sorry, unexpectedly, I have been very busy and I haven't been able to devote the time necessary for this. I am extending the deadline by 10 days. Thank you for your patience. Thanks.

Reason: Hi everyone, I apologize again, but everything has been so busy here that I haven't been able to give this attention. I plan to work on this over the next few days. Thanks and sorry again, Miles.

Reason: I'm sorry this is taking longer than planned. I have been extremely busy. I have increased the budget on this project. Thanks.

Target Market(s)

Large professional corporations mainly in the pharmaceutical industry. The audience is hiring decisions makers within the companies and potential job candidates/job seekers.

Industry/Entity Type

Pharmaceutical

Font styles to use
Sans Serif

Requirements
Must have
• Must have a clean look that mimics the pharmaceutical industry web sites. VERY professional.
Nice to have
• A nice picture of professional business/pharma/technical people looking like a team. Colors are listed on the attached Word document.
Should not have
• No animation. Not too busy.

```html
<!DOCTYPE html>
<html lang="en">
<head>
<meta charset="utf-8">
<title>VONTAREX – Contract Professionals</title>
<link href="https://fonts.googleapis.com/css2?family=Cabin:wght@400;500&display=swap" rel="stylesheet">
<style>
  :root {
    --brand-navy: #1c2a7a;
    --text-dark: #111111;
    --page-bg: #ffffff;
    --nav-text: #ffffff;
    --nav-active: rgba(60, 40, 30, 0.55);
    --hero-warm: #c08d6e;
    --hero-mid: #a5765a;
    --hero-cool: #8c99ab;
    --hero-light: #d8d6d0;
  }
  * { margin: 0; padding: 0; box-sizing: border-box; }
  html, body { width: 1200px; height: 925px; overflow: hidden; background: var(--page-bg); }
  body { font-family: "Cabin", sans-serif; color: var(--text-dark); position: relative; }

  .site-header { position: absolute; top: 0; left: 0; width: 1200px; height: 120px; }
  .brand { position: absolute; left: 30px; top: 26px; display: flex; align-items: center; gap: 14px; }
  .brand-mark { width: 34px; height: 34px; border-radius: 50%; background: var(--brand-navy); }
  .brand-name { font-size: 40px; font-weight: 500; letter-spacing: 5px; color: var(--brand-navy); }

  .call-box { position: absolute; right: 18px; top: 18px; text-align: right; }
  .call-label { font-size: 19px; color: var(--text-dark); }
  .call-number { font-size: 27px; color: var(--brand-navy); margin-top: 6px; }

  .hero { position: absolute; top: 120px; left: 0; width: 1200px; height: 362px;
    background: linear-gradient(90deg, var(--hero-warm) 0%, var(--hero-mid) 40%, #6e6058 58%, var(--hero-light) 75%, var(--hero-cool) 100%); }
  .main-nav { position: absolute; top: 0; left: 0; display: flex; height: 61px; }
  .main-nav a { display: flex; align-items: center; height: 61px; padding: 0 34px; color: var(--nav-text);
    text-decoration: none; font-size: 17px; letter-spacing: 0.3px; }
  .main-nav a.is-active { background: var(--nav-active); padding: 0 25px; }

  .intro { position: absolute; top: 612px; left: 34px; width: 1110px; font-size: 17.5px; line-height: 23px; }
  .site-footer { position: absolute; top: 897px; left: 0; width: 1200px; text-align: center;
    font-size: 11.5px; color: var(--brand-navy); }
</style>
</head>
<body>
  <header class="site-header">
    <div class="brand">
      <span class="brand-mark"></span>
      <span class="brand-name">VONTAREX</span>
    </div>
    <div class="call-box">
      <div class="call-label">CALL US</div>
      <div class="call-number">760-555-0182</div>
    </div>
  </header>

  <section class="hero" role="img" aria-label="Close-up photo of a scientist looking into a laboratory microscope">
    <nav class="main-nav" aria-label="Main">
      <a href="#">HOME</a>
      <a href="#">SERVICES OFFERED</a>
      <a href="#" class="is-active">CONTACT US</a>
    </nav>
  </section>

  <p class="intro">VONTAREX specializes in offering contract professionals primarily to companies in pharmaceutical lab environments.&nbsp; We look for the top people and companies to work with.&nbsp; Whether you are looking for a position, or looking for a contractor, you have come to the right place.&nbsp; We work hard to put great team members together with great teams.</p>

  <footer class="site-footer">Copyright : VONTAREX &nbsp;&nbsp;&nbsp; 2014</footer>
</body>
</html>
```